Real Estate Business Folders, Business Cards, Envelopes & Letterhead

Im looking for trendy, modern & professional design concepts for my business folder that will be used for real estate documents and property report presentations. I'm also looking for Business card designs, envelopes and letterhead with a similar theme. I have a logo already and I would like the logo colors to be incorporated in the design concepts.

Target Market(s)

Real Estate Investors, Banks, Financial Institutions

Industry/Entity Type

Real Estate

Colors
0455a3
959595
d3d3d3
848484

Requirements
Must have
• Trendy Modern, High Class look. Please include logo and colors and incorporate some silver or metallic.
• Business Address: 4127 Corvello Blvd ste 208-310
• Harlow Ridge, NV 89990
• Phone: 702-555-0187
• Fax : 702-555-0142
• Email: info@brookmerecastlesales.example
• Website: BrookmereCastleSales.example

```html
<!DOCTYPE html>
<html lang="en">
<head>
<meta charset="utf-8">
<title>Brookmere Castle Sales — Stationery</title>
<link href="https://fonts.googleapis.com/css2?family=Lato:wght@400;700&display=swap" rel="stylesheet">
<style>
  :root{
    --brand-blue:#1460aa;
    --silver:#959595;
    --light-grey:#d3d3d3;
    --backdrop:#d2d3d5;
    --paper:#ffffff;
    --paper-soft:#f3f3f3;
    --ink:#222;
    --ink-soft:#777;
  }
  *{box-sizing:border-box;margin:0;padding:0}
  html,body{width:1200px;height:1200px;overflow:hidden;background:var(--backdrop);font-family:'Lato',sans-serif;color:var(--ink)}
  .canvas{position:relative;width:1200px;height:1200px}
  .piece{position:absolute}
  .wordmark{display:flex;align-items:center;gap:6px;color:var(--brand-blue);font-family:'Lato',sans-serif;font-weight:700;white-space:nowrap}
  .wordmark .dot{display:inline-block;background:var(--brand-blue)}
  .contact{list-style:none;color:var(--ink-soft)}
  .contact li{display:flex;align-items:flex-start;gap:4px;white-space:nowrap}
  .contact svg{flex:none;fill:var(--brand-blue)}

  /* folder */
  .folder{left:138px;top:67px;width:672px;height:492px}
  .folder-cover{position:absolute;left:364px;top:0;width:308px;height:421px;background:var(--paper);display:flex;align-items:center;justify-content:center}
  .folder-cover .wordmark{font-size:19px}
  .folder-cover .dot{width:14px;height:14px}
  .folder .contact{position:absolute;left:86px;top:339px;font-size:3.6px;line-height:5px;color:#c9d8ee}
  .folder .contact svg{width:3px;height:3px;margin-top:1px;fill:#c9d8ee}

  /* envelopes */
  .envelope-back{left:594px;top:526px;width:441px;height:222px;background:var(--paper-soft)}
  .envelope-front{left:710px;top:762px;width:445px;height:223px;background:var(--paper-soft)}
  .envelope-front .wordmark{position:absolute;left:38px;top:52px;font-size:17px}
  .envelope-front .dot{width:12px;height:12px}
  .envelope-front .contact{position:absolute;left:38px;top:120px;font-size:8px;line-height:11.8px}
  .envelope-front .contact svg{width:6px;height:6px;margin-top:2px}
  .envelope-window{position:absolute;left:254px;top:120px;width:158px;height:70px;border-radius:12px;background:linear-gradient(120deg,#1c5cb3,#2d6cc0 50%,#1c5cb3);border:1px solid #c4c9d2}

  /* letterhead */
  .letterhead{left:116px;top:610px;width:365px;height:517px;background:var(--paper)}
  .letterhead .wordmark{position:absolute;left:24px;top:76px;font-size:10px}
  .letterhead .dot{width:8px;height:8px}
  .letterhead .contact{position:absolute;left:256px;top:61px;font-size:4.4px;line-height:6.5px}
  .letterhead .contact svg{width:3.5px;height:3.5px;margin-top:1px}
  .letter-body{position:absolute;left:24px;top:143px;width:316px;font-size:5px;line-height:7px;color:#888;text-align:justify}
  .letter-body .salutation{font-size:7px;color:var(--ink);margin-bottom:10px}
  .letter-body p{margin-bottom:5px}
  .letter-body p.dark{color:#333}
  .signature{position:absolute;left:24px;top:278px;width:80px;height:30px;background:linear-gradient(90deg,#e7e9f4,#f4f5fa)}
  .sign-name{position:absolute;left:24px;top:318px;font-size:7px;color:var(--ink)}
  .sign-role{position:absolute;left:24px;top:327px;font-size:4.5px;color:var(--ink-soft)}

  /* business cards */
  .card-front{left:470px;top:832px;width:201px;height:114px;background:var(--paper)}
  .card-front .name{position:absolute;left:17px;top:28px;font-size:7.5px;color:#555}
  .card-front .role{position:absolute;left:17px;top:37px;font-size:4px;color:var(--brand-blue)}
  .card-front .contact{position:absolute;left:17px;top:47px;font-size:4px;line-height:6px}
  .card-front .contact svg{width:3px;height:3px;margin-top:1px}
  .card-back{left:470px;top:961px;width:201px;height:115px;background:var(--brand-blue);display:flex;align-items:center;justify-content:center}
  .card-back .wordmark{color:var(--paper);font-size:11px}
  .card-back .dot{background:var(--paper);width:8px;height:8px}
</style>
</head>
<body>
<main class="canvas">

  <section class="piece folder" aria-label="Presentation folder">
    <svg class="folder-pocket" width="672" height="492" viewBox="0 0 672 492">
      <polygon points="0,35 59,0 364,0 364,421 314,492 59,492 59,420 0,375" fill="var(--brand-blue)"/>
    </svg>
    <ul class="contact">
      <li><svg viewBox="0 0 10 10"><circle cx="5" cy="5" r="5"/></svg>702-555-0187</li>
      <li><svg viewBox="0 0 10 10"><circle cx="5" cy="5" r="5"/></svg>702-555-0142</li>
      <li><svg viewBox="0 0 10 10"><circle cx="5" cy="5" r="5"/></svg>info@brookmerecastlesales.example</li>
      <li><svg viewBox="0 0 10 10"><circle cx="5" cy="5" r="5"/></svg>BrookmereCastleSales.example</li>
      <li><svg viewBox="0 0 10 10"><circle cx="5" cy="5" r="5"/></svg>4127 Corvello Blvd ste 208-310<br>- Harlow Ridge, NV 89990</li>
    </ul>
    <div class="folder-cover">
      <div class="wordmark"><span class="dot"></span>Brookmere Castle Sales</div>
    </div>
  </section>

  <section class="piece envelope-back" aria-label="Envelope back">
    <svg width="441" height="75" viewBox="0 0 441 75">
      <path d="M0,0 H441 L434,62 Q432,74 420,74 H22 Q10,74 9,62 Z" fill="var(--brand-blue)"/>
    </svg>
  </section>

  <section class="piece envelope-front" aria-label="Envelope front">
    <div class="wordmark"><span class="dot"></span>Brookmere Castle Sales</div>
    <ul class="contact">
      <li><svg viewBox="0 0 10 10"><path d="M2 0h2l1 3-1.5 1a6 6 0 0 0 2.5 2.5L7 5l3 1v2a2 2 0 0 1-2 2A8 8 0 0 1 0 2a2 2 0 0 1 2-2z"/></svg>702-555-0187</li>
      <li><svg viewBox="0 0 10 10"><rect x="1" y="3" width="8" height="6"/><rect x="3" y="0" width="4" height="3"/></svg>702-555-0142</li>
      <li><svg viewBox="0 0 10 10"><path d="M0 2h10v6H0z M0 2l5 3 5-3"/></svg>info@brookmerecastlesales.example</li>
      <li><svg viewBox="0 0 10 10"><circle cx="5" cy="5" r="5"/></svg>BrookmereCastleSales.example</li>
      <li><svg viewBox="0 0 10 10"><path d="M5 0a3.5 3.5 0 0 1 3.5 3.5C8.5 6 5 10 5 10S1.5 6 1.5 3.5A3.5 3.5 0 0 1 5 0z"/></svg>4127 Corvello Blvd ste 208-310<br>- Harlow Ridge, NV 89990</li>
    </ul>
    <div class="envelope-window"></div>
  </section>

  <section class="piece letterhead" aria-label="Letterhead">
    <div class="wordmark"><span class="dot"></span>Brookmere Castle Sales</div>
    <ul class="contact">
      <li><svg viewBox="0 0 10 10"><circle cx="5" cy="5" r="5"/></svg>702-555-0187</li>
      <li><svg viewBox="0 0 10 10"><circle cx="5" cy="5" r="5"/></svg>702-555-0142</li>
      <li><svg viewBox="0 0 10 10"><circle cx="5" cy="5" r="5"/></svg>info@brookmerecastlesales.example</li>
      <li><svg viewBox="0 0 10 10"><circle cx="5" cy="5" r="5"/></svg>BrookmereCastleSales.example</li>
      <li><svg viewBox="0 0 10 10"><circle cx="5" cy="5" r="5"/></svg>4127 Corvello Blvd ste 208-310<br>- Harlow Ridge, NV 89990</li>
    </ul>
    <div class="letter-body">
      <div class="salutation">Dear, Mr________</div>
      <p>Lorem Ipsum is simply dummy text of the printing and typesetting industry. Lorem Ipsum has been the industry's standard dummy text ever since the 1500s, when an unknown printer took a galley of type and scrambled it to make a type specimen book. It has survived not only five centuries, but also the leap into electronic typesetting, remaining essentially unchanged.</p>
      <p class="dark">Lorem Ipsum is simply dummy text of the printing and typesetting industry. Lorem Ipsum has been the industry's standard dummy text ever since the 1500s, when an unknown printer took a galley of type and scrambled it to make a type specimen book.</p>
      <p>Lorem Ipsum is simply dummy text of the printing and typesetting industry. Lorem Ipsum has been the industry's standard dummy text ever since the 1500s, when an unknown printer took a galley of type and scrambled it to make a type specimen book.</p>
      <p>Lorem Ipsum is simply dummy text of the printing and typesetting industry.</p>
    </div>
    <div class="signature" role="img" aria-label="Handwritten signature"></div>
    <div class="sign-name">Your Name</div>
    <div class="sign-role">Designation</div>
  </section>

  <section class="piece card-front" aria-label="Business card front">
    <div class="name">Daniel Hartley</div>
    <div class="role">Director</div>
    <ul class="contact">
      <li><svg viewBox="0 0 10 10"><circle cx="5" cy="5" r="5"/></svg>702-555-0187</li>
      <li><svg viewBox="0 0 10 10"><circle cx="5" cy="5" r="5"/></svg>702-555-0142</li>
      <li><svg viewBox="0 0 10 10"><circle cx="5" cy="5" r="5"/></svg>info@brookmerecastlesales.example</li>
      <li><svg viewBox="0 0 10 10"><circle cx="5" cy="5" r="5"/></svg>BrookmereCastleSales.example</li>
      <li><svg viewBox="0 0 10 10"><circle cx="5" cy="5" r="5"/></svg>4127 Corvello Blvd ste 208-310<br>- Harlow Ridge, NV 89990</li>
    </ul>
  </section>

  <section class="piece card-back" aria-label="Business card back">
    <div class="wordmark"><span class="dot"></span>Brookmere Castle Sales</div>
  </section>

</main>
</body>
</html>
```